Start-up braucht modernes/hochwertiges Getränkeetikett
Zielgruppe
Wir sind ein modernes, nachhaltiges Start-up, welches eine neue Getränkekategorie auf den Markt bringt. Ein sogenanntes Elektrolyt-Getränk mit dem Namen KLORV5. Es ist abgefüllt in eine 500 ml Flasche und enthält Magnesium, Kalzium, Kalium, und Natrium. Diese Stoffe (Elektrolyte) dienen der körperlichen Hydrierung. Zu Dehydrierung kann es durch Hitze, Alkohol, Sport oder Krankheit kommen. Krankheit liegt bei uns allerdings nicht im Fokus. In unserer Zielgruppe befinden sich hauptsächlich Personen im Alter von 18 - 29 Jahren.
Die Geschmacksrichtung ist Zitrone-Limette.
Aufgabenstellung
Das Etikett soll:
- MODERN, SCHLICHT und HOCHWERTIG sein, so dass es im Supermarkt hervorsticht
- erkenntlich machen, dass die Stoffe Magnesium, Natrium, Kalzium und Kalium enthalten sind
- sich farblich deutlich von der Farbe des Inhalts (weiß) abheben. (Vorzugsweise mit einem hellen Blau, türkis)
- für unsere junge Zielgruppe ansprechend sein
- ebenfalls auf die Geschmacksrichtung (Zitrone-Limette) hinweisen, und zwar so, dass wenn man eine weitere Geschmacksrichtung auf den Markt bringen möchte, diese leicht angepasst werden kann.
- nicht nach einem Energydrink oder einem typischen Sportgetränk aussehen
- unter dem Namen den Slogan 'Elektrolyt-Getränk' stehen haben
-Das Etikett ist nicht dursichtig sondern besteht aus Papier
Der Name sowie das Logo können selbstverständlich farblich verändert werden. Bei dem Logo können auch größere Änderungen vollzogen werden.
Bitte beachten Sie die unten zu stehenden Regler um sich einen guten Überblick über unsere Vorstellungen zu verschaffen. Die Platzierung des EAN-Code ist für ihr Design irrelevat .
Bei Unklarheiten gerne nachfragen!

```html
<!DOCTYPE html>
<html lang="de">
<head>
<meta charset="utf-8">
<title>KLORV5 Etikett</title>
<link rel="stylesheet" href="https://fonts.googleapis.com/css2?family=Montserrat:wght@400;700&family=Rubik+Dirt&family=Titillium+Web:wght@700&family=Archivo+Black&display=swap">
<style>
  :root {
    --paper: #ffffff;
    --ice: #b8c8df;
    --ice-light: #dbe4f0;
    --glow: #ffffff;
    --ink: #1c1c1c;
    --lime: #b5c92f;
    --drop-top: #c8d52a;
    --drop-bottom: #e4e233;
    --brand: #c2d0e3;
  }
  html, body {
    margin: 0;
    padding: 0;
    width: 1200px;
    height: 522px;
    overflow: hidden;
    background: var(--paper);
  }
  .label {
    position: relative;
    width: 1200px;
    height: 522px;
    background: var(--paper);
    font-family: "Montserrat", sans-serif;
    color: var(--ink);
  }
  .ice-field {
    position: absolute;
    inset: 0;
  }
  .element {
    position: absolute;
    left: 102px;
    width: 40px;
    writing-mode: vertical-rl;
    transform: rotate(180deg);
    font-family: "Rubik Dirt", sans-serif;
    font-size: 40px;
    line-height: 40px;
    color: var(--ink);
    text-align: center;
  }
  .element sup { font-size: 22px; vertical-align: super; line-height: 0; }
  .element--k  { top: 42px;  height: 46px; }
  .element--ca { top: 150px; height: 92px; }
  .element--na { top: 280px; height: 92px; }
  .element--mg { top: 408px; height: 98px; }

  .text-block {
    position: absolute;
    width: 178px;
    font-size: 15px;
    line-height: 27.2px;
    text-align: justify;
    margin: 0;
  }
  .text-block h2 {
    font-size: 15px;
    font-weight: 700;
    margin: 0;
    line-height: 27.2px;
    text-align: left;
  }
  .electrolytes { left: 230px; top: 18px; }
  .nutrition { left: 857px; top: 18px; }
  .ingredients { left: 857px; top: 236px; }
  .company { left: 230px; top: 344px; }
  .company p { margin: 0; }
  .text-block .last { text-align-last: left; }

  .volume {
    position: absolute;
    left: 953px;
    top: 476px;
    font-weight: 700;
    font-size: 22px;
    margin: 0;
  }
  .drop {
    position: absolute;
    left: 595px;
    top: 198px;
  }
  .flavour {
    position: absolute;
    left: 490px;
    top: 360px;
  }
  .flavour-text {
    position: absolute;
    left: 540px;
    top: 380px;
    transform: rotate(-4deg);
    font-family: "Titillium Web", sans-serif;
    font-weight: 700;
    font-size: 22px;
    line-height: 24px;
    color: var(--paper);
    margin: 0;
  }
  .brand {
    position: absolute;
    left: 1063px;
    top: 98px;
    width: 66px;
    height: 325px;
    writing-mode: vertical-rl;
    transform: rotate(180deg);
    font-family: "Archivo Black", sans-serif;
    font-size: 66px;
    line-height: 66px;
    color: var(--brand);
    text-align: center;
    margin: 0;
  }
  .slogan {
    position: absolute;
    left: 1148px;
    top: 102px;
    width: 34px;
    height: 320px;
    writing-mode: vertical-rl;
    transform: rotate(180deg);
    font-family: "Montserrat", sans-serif;
    font-weight: 700;
    font-size: 29px;
    line-height: 34px;
    color: var(--brand);
    text-align: center;
    margin: 0;
  }
</style>
</head>
<body>
<main class="label">
  <svg class="ice-field" width="1200" height="522" viewBox="0 0 1200 522" role="img" aria-label="Hellblaue Fläche mit Eisrissen, in der Mitte weiß aufleuchtend">
    <defs>
      <radialGradient id="iceGlow" cx="634" cy="272" r="420" gradientUnits="userSpaceOnUse">
        <stop offset="0" stop-color="var(--glow)"/>
        <stop offset="0.22" stop-color="var(--glow)"/>
        <stop offset="0.5" stop-color="var(--ice-light)"/>
        <stop offset="0.85" stop-color="var(--ice)"/>
      </radialGradient>
    </defs>
    <path d="M158 0 L1064 0 L1064 522 L158 522 L196 456 L158 391 L196 326 L158 259 L196 194 L158 130 L196 65 Z" fill="url(#iceGlow)"/>
  </svg>

  <div class="element element--k">K<sup>+</sup></div>
  <div class="element element--ca">Ca<sup>2+</sup></div>
  <div class="element element--na">Na<sup>2+</sup></div>
  <div class="element element--mg">Mg<sup>2+</sup></div>

  <section class="text-block electrolytes">
    <h2>Elektrolyte</h2>
    <p class="last" style="margin:0">dolor sit amet, consec­tetuer adipiscing elit, sed diam non ummy nibh euiss Lorem ipsum dolor sit amet, consectetuer.</p>
  </section>

  <section class="text-block company">
    <p>Musterfirma GmbH</p>
    <p>Musterstr. 12</p>
    <p>12345 Musterstadt</p>
    <p>Gekühlt genießen!</p>
    <p class="last">Trocken, kühl und lichtgeschützt lagern.</p>
  </section>

  <section class="text-block nutrition">
    <h2>Nährwertinformation</h2>
    <p class="last" style="margin:0">dolor sit amet, consec­tetuer adipiscing elit, sed diam non ummy nibh euiss Lorem ipsum dolor sit amet, consectetuer</p>
  </section>

  <p class="text-block ingredients last">Zutaten: ipsum dolor sit amet, consectetuer adipiscing elit, sed diam onummy nibh eui Lorem ipsum dolor sit amet, consectetuer</p>

  <p class="volume">500ml</p>

  <svg class="drop" width="78" height="126" viewBox="0 0 78 126" aria-hidden="true">
    <defs>
      <linearGradient id="dropFill" x1="0" y1="0" x2="0" y2="1">
        <stop offset="0" stop-color="var(--drop-top)"/>
        <stop offset="0.55" stop-color="var(--lime)"/>
        <stop offset="1" stop-color="var(--drop-bottom)"/>
      </linearGradient>
    </defs>
    <path d="M39 0 C50 22 62 40 72 62 C76 70 78 76 78 86 C78 108 60 126 39 126 C18 126 0 108 0 86 C0 76 2 70 6 62 C16 40 28 22 39 0 Z" fill="url(#dropFill)"/>
  </svg>

  <svg class="flavour" width="300" height="110" viewBox="0 0 300 110" aria-hidden="true">
    <g fill="var(--lime)">
      <polygon points="34,24 242,12 290,2 294,42 258,45 264,60 278,58 277,66 256,68 258,84 50,104 46,90 12,92 20,60 32,58"/>
      <polygon points="16,98 230,80 230,84 18,102"/>
      <polygon points="40,108 240,92 240,96 42,112"/>
    </g>
  </svg>
  <p class="flavour-text">Limette-Zitronen<br>Geschmack</p>

  <h1 class="brand">KLORV5</h1>
  <p class="slogan">Elektrolyt-Getränk</p>
</main>
</body>
</html>
```